Velmora and Co Business Card Design

Looking for a business card design. Wanting Smart, Clean and Sharp looking to promote Velmora and Co, our Import Export Business - like Black, White and natural textures. I have uploaded our logo. I like a rounded font but open to other ideas
Being that we have a wide range of products on offer we are looking for a neutral yet eye catching card. We would also like to have Import - Export on the business card to be clear on want our business does.

Target Market(s)

Import export market

Industry/Entity Type

Importer

Contact Information for Business Card

Mr Tobias Kernwell
tobias.kernwell@velmoraandco.com.au
+61 (0) 417 630 284
www.velmoraandco.com.au

Font styles to use
Other font styles liked:
• Unsure of actual font name but something rounded and clean

Colors

Designer to choose colors to be used in the design.

Requirements
Must have
• Instagram icon
• Facebook icon

```html
<!DOCTYPE html>
<html lang="en">
<head>
<meta charset="utf-8">
<title>Velmora and Co – Business Card</title>
<link rel="stylesheet" href="https://fonts.googleapis.com/css2?family=Oswald:wght@500&family=Lato:wght@300;400&display=swap">
<style>
  :root {
    --backdrop: #3a332f;
    --card: #0d0d0d;
    --card-edge: #1a1a1a;
    --ink: #f2f2f2;
    --ink-soft: #c9c9c9;
    --silver: #d6d6d6;
    --rule: #4a4a4a;
  }
  * { margin: 0; padding: 0; box-sizing: border-box; }
  html, body {
    width: 1200px; height: 844px; overflow: hidden;
    background: var(--backdrop);
  }
  .stage {
    position: relative; width: 1200px; height: 844px;
    display: flex; align-items: center; justify-content: center; gap: 60px;
  }
  .card {
    position: relative; width: 520px; height: 318px;
    background: var(--card);
    border: 1px solid var(--card-edge);
    box-shadow: 0 10px 30px rgba(0,0,0,.45);
  }

  /* Contact side */
  .card--contact .brand {
    position: absolute; left: 40px; top: 0; bottom: 0; width: 200px;
    display: flex; align-items: center; gap: 10px;
  }
  .brand__mark {
    width: 18px; height: 18px; background: var(--ink); flex: none;
  }
  .brand__name {
    font-family: "Oswald", sans-serif; font-weight: 500;
    font-size: 26px; line-height: 1.05; letter-spacing: 1px;
    color: var(--ink); text-transform: uppercase;
  }
  .card--contact .divider {
    position: absolute; left: 252px; top: 40px; bottom: 40px;
    width: 1px; background: var(--rule);
  }
  .details {
    position: absolute; left: 276px; top: 92px; right: 16px;
  }
  .details__name {
    font-family: "Oswald", sans-serif; font-weight: 500;
    font-size: 17px; letter-spacing: .5px; color: var(--ink);
    text-transform: uppercase; margin-bottom: 34px;
  }
  .details__list { list-style: none; }
  .details__item {
    display: flex; align-items: center; gap: 7px;
    font-family: "Lato", sans-serif; font-weight: 300;
    font-size: 12px; line-height: 18px; color: var(--ink-soft);
    white-space: nowrap;
  }
  .details__item svg { width: 11px; height: 11px; flex: none; }

  /* Logo side */
  .card--logo .brand {
    position: absolute; left: 0; right: 0; top: 62px;
    display: flex; justify-content: center; align-items: center; gap: 10px;
  }
  .card--logo .brand__mark { background: var(--silver); }
  .card--logo .brand__name { color: var(--silver); font-size: 28px; }
  .rule {
    position: absolute; height: 1px; background: var(--rule);
  }
  .rule--upper { left: 290px; right: 40px; top: 150px; }
  .rule--lower { left: 110px; right: 230px; top: 232px; }
  .social {
    position: absolute; left: 0; right: 0; top: 180px;
    display: flex; justify-content: center; gap: 8px;
  }
  .social__icon {
    width: 20px; height: 20px; background: var(--ink);
  }
</style>
</head>
<body>
<main class="stage">
  <section class="card card--contact" aria-label="Contact side">
    <div class="brand">
      <span class="brand__mark"></span>
      <span class="brand__name">Velmora<br>&amp; Co</span>
    </div>
    <div class="divider"></div>
    <div class="details">
      <p class="details__name">Mr Tobias Kernwell</p>
      <ul class="details__list">
        <li class="details__item">
          <svg viewBox="0 0 12 12" aria-hidden="true"><path d="M1 4.5c0-1.5 2-2.5 5-2.5s5 1 5 2.5v1H8.5V4.3H3.5v1.2H1z M3 6h6l1 4H2z" fill="#c9c9c9"/></svg>
          +61 (0) 417 630 284
        </li>
        <li class="details__item">
          <svg viewBox="0 0 12 12" aria-hidden="true"><rect x="1" y="2.5" width="10" height="7" fill="none" stroke="#c9c9c9" stroke-width="1.2"/><path d="M1 2.5l5 4 5-4" fill="none" stroke="#c9c9c9" stroke-width="1.2"/></svg>
          tobias.kernwell@velmoraandco.com.au
        </li>
        <li class="details__item">
          <svg viewBox="0 0 12 12" aria-hidden="true"><circle cx="6" cy="6" r="5" fill="#c9c9c9"/><path d="M1 6h10M6 1c-2 2.5-2 7.5 0 10M6 1c2 2.5 2 7.5 0 10" fill="none" stroke="#0d0d0d" stroke-width=".8"/></svg>
          www.velmoraandco.com.au
        </li>
      </ul>
    </div>
  </section>

  <section class="card card--logo" aria-label="Logo side">
    <div class="brand">
      <span class="brand__mark"></span>
      <span class="brand__name">Velmora<br>&amp; Co</span>
    </div>
    <div class="rule rule--upper"></div>
    <div class="social">
      <span class="social__icon" role="img" aria-label="Social profile icon"></span>
      <span class="social__icon" role="img" aria-label="Social profile icon"></span>
    </div>
    <div class="rule rule--lower"></div>
  </section>
</main>
</body>
</html>
```